Vintage Old-fashion Style Gin Bottle Label

I am opening a distillery in England next year and I need a label for my first product - gin. There will be several new labels required for new products in the future for the designer.
Please see attachments as examples of the style of branding and label I am looking for. In particular, I really like the style of the Harwell Vine Traders label (see reference 1 and 2), so I would like something similar in style to that, with words in difference directions and lots of detailing.
In terms of colour, I would like dark blue.
The distillery will be located inside a converted railway arch on Foundry Lane in Manchester, England. Please incorporate railway arches into the design.
Dimensions for this label are approximately 15cm X 15cm, although this is flexible. Shape is flexible.
Part of this label design includes a bottle seal label. Please see attachment labelled bottle seal label.
The main label must contain the following information. I have included a few guidelines for the size of some words but there is also a lot of flexibility.
TRASKE DISTILLING CO.
(company name - large font)
KEEPERS OF NORTHERN CRAFT
(company motto)
GIN (product - large font)
SUPERIOR QUALITY (written small just above GIN)
MADE IN MANCHESTER
EST. MMXX
UNIQUELY DISTILLED & ARTFULLY BLENDED
HANDCRAFTED PREMIUM LIQUOR
PRODUCED IN SMALL BATCHES
CREATED USING OUR BESPOKE COPPER MOONSHINE STILL
45%ABV
70CL
PRODUCT OF ENGLAND
TRASKE DISTILLING COMPANY, 41 FOUNDRY LANE, MANCHESTER M4 9RD ENGLAND (address)
APPROVED BY:
W. TRASKE
(please include my attached signature near this)
If you have any questions at all, at any stage through your design, please let me know. I will try to answer them very quickly.
I look forward to seeing your design.
Sincerely,
Walter
Requirements
Must have
- Must have all the words mentioned in brief.
- Must also include an image of railway arches.

```html
<!DOCTYPE html>
<html lang="en">
<head>
<meta charset="utf-8">
<title>Traske Distilling Co. — Gin Label</title>
<link rel="stylesheet" href="https://fonts.googleapis.com/css2?family=Rye&family=Oswald:wght@400;600&family=IM+Fell+English+SC&display=swap">
<style>
  :root {
    --page: #f4f4f2;
    --paper: #dcdad2;
    --navy: #1d2333;
    --pattern: #9b9ea6;
    --shade: #5a6070;
  }
  html, body {
    margin: 0;
    width: 900px;
    height: 1200px;
    overflow: hidden;
    background: var(--page);
  }
  .label {
    position: absolute;
    left: 120px;
    top: 164px;
    width: 660px;
    height: 872px;
  }
  .label-paper { fill: var(--paper); }
  .rule { fill: none; stroke: var(--navy); }
  .navy-fill { fill: var(--navy); }
  .pattern-area { fill: var(--pattern); }
  .brand-name {
    font-family: "Rye", serif;
    font-size: 34px;
    fill: var(--navy);
  }
  .product-name {
    font-family: "Oswald", sans-serif;
    font-weight: 600;
    font-size: 54px;
    fill: var(--navy);
  }
  .serif-caps {
    font-family: "IM Fell English SC", serif;
    fill: var(--navy);
  }
  .small-caps {
    font-family: "Oswald", sans-serif;
    font-weight: 600;
    fill: var(--navy);
  }
  .plain-caps {
    font-family: "Oswald", sans-serif;
    font-weight: 400;
    fill: var(--navy);
  }
  .on-navy { fill: var(--paper); }
</style>
</head>
<body>
<svg class="label" viewBox="0 0 420 555" xmlns="http://www.w3.org/2000/svg" aria-label="Traske Distilling Co. gin label">
  <defs>
    <path id="motto-arc" d="M70 142 Q210 20 350 142"/>
    <path id="superior-arc" d="M80 330 Q210 450 340 330"/>
    <path id="blend-arc" d="M92 362 Q210 478 328 362"/>
  </defs>

  <!-- paper and frames -->
  <rect class="label-paper" x="0" y="0" width="420" height="555"/>
  <rect class="rule" x="5" y="5" width="410" height="545" stroke-width="3"/>
  <rect class="rule" x="11" y="11" width="398" height="533" stroke-width="1"/>

  <!-- decorative corner and side patterns -->
  <rect class="pattern-area" x="14" y="14" width="66" height="100" role="img" aria-label="Ornamental lattice pattern, top left corner"/>
  <rect class="pattern-area" x="340" y="14" width="66" height="100" role="img" aria-label="Ornamental lattice pattern, top right corner"/>
  <rect class="pattern-area" x="14" y="308" width="60" height="110" role="img" aria-label="Ornamental lattice pattern, left side"/>
  <rect class="pattern-area" x="346" y="308" width="60" height="110" role="img" aria-label="Ornamental lattice pattern, right side"/>

  <!-- est -->
  <text class="serif-caps" x="210" y="36" font-size="12" text-anchor="middle">EST. MMXX</text>

  <!-- motto banner -->
  <path d="M70 142 Q210 20 350 142" fill="none" stroke="var(--navy)" stroke-width="24"/>
  <path d="M70 142 Q210 20 350 142" fill="none" stroke="var(--paper)" stroke-width="20"/>
  <text class="serif-caps" font-size="12.5" letter-spacing="1">
    <textPath href="#motto-arc" startOffset="50%" text-anchor="middle" dominant-baseline="middle">KEEPERS OF NORTHERN CRAFT</textPath>
  </text>

  <!-- railway arches -->
  <rect class="pattern-area" x="140" y="114" width="140" height="56" role="img" aria-label="Illustration of a Victorian railway viaduct with a row of brick arches"/>
  <line class="rule" x1="110" y1="176" x2="310" y2="176" stroke-width="2"/>
  <line class="rule" x1="120" y1="181" x2="300" y2="181" stroke-width="1"/>

  <!-- brand name -->
  <text class="brand-name" x="210" y="222" text-anchor="middle" textLength="392" lengthAdjust="spacingAndGlyphs">TRASKE DISTILLING CO.</text>

  <!-- info row -->
  <text class="small-caps" x="18" y="260" font-size="10">MADE IN</text>
  <text class="small-caps" x="18" y="272" font-size="9">MANCHESTER</text>
  <rect class="navy-fill" x="92" y="252" width="236" height="22"/>
  <text class="plain-caps on-navy" x="210" y="267" font-size="10.5" text-anchor="middle">UNIQUELY DISTILLED &amp; ARTFULLY BLENDED</text>
  <text class="small-caps" x="404" y="268" font-size="14" text-anchor="end">45%ABV</text>

  <rect class="rule" x="100" y="282" width="220" height="18" stroke-width="1"/>
  <rect fill="var(--shade)" x="102" y="284" width="216" height="14"/>
  <text class="small-caps on-navy" x="210" y="295" font-size="9.5" text-anchor="middle" letter-spacing="1.5">PRODUCED IN SMALL BATCHES</text>

  <!-- gin emblem -->
  <path d="M80 330 Q210 450 340 330" fill="none" stroke="var(--navy)" stroke-width="20"/>
  <text class="serif-caps on-navy" font-size="9.5">
    <textPath href="#superior-arc" startOffset="18%" text-anchor="middle" dominant-baseline="middle">SUPERIOR</textPath>
  </text>
  <text class="serif-caps on-navy" font-size="9.5">
    <textPath href="#superior-arc" startOffset="82%" text-anchor="middle" dominant-baseline="middle">QUALITY</textPath>
  </text>
  <text class="product-name" x="210" y="372" text-anchor="middle" letter-spacing="2">GIN</text>

  <path d="M92 362 Q210 478 328 362" fill="none" stroke="var(--navy)" stroke-width="22"/>
  <text class="serif-caps on-navy" font-size="10.5">
    <textPath href="#blend-arc" startOffset="50%" text-anchor="middle" dominant-baseline="middle">UNIQUELY DISTILLED &amp; ARTFULLY BLENDED</textPath>
  </text>

  <!-- lower details -->
  <text class="serif-caps" x="86" y="447" font-size="7.5">CREATED USING OUR BESPOKE COPPER MOONSHINE STILL</text>
  <line class="rule" x1="84" y1="450" x2="344" y2="450" stroke-width="0.8"/>

  <circle class="navy-fill" cx="36" cy="474" r="20"/>
  <circle fill="none" stroke="var(--paper)" stroke-width="0.8" cx="36" cy="474" r="17"/>
  <text class="small-caps on-navy" x="36" y="478" font-size="11" text-anchor="middle">70 CL</text>

  <path class="rule" d="M62 462 H270 L280 474 L270 486 H62" stroke-width="1"/>
  <text class="serif-caps" x="68" y="479" font-size="13.5">PRODUCT OF ENGLAND</text>
  <line class="rule" x1="280" y1="474" x2="288" y2="474" stroke-width="1"/>

  <text class="plain-caps" font-size="7">
    <tspan x="292" y="461">TRASKE DISTILLING COMPANY,</tspan>
    <tspan x="300" y="471">41 FOUNDRY LANE,</tspan>
    <tspan x="300" y="481">MANCHESTER M4 9RD</tspan>
    <tspan x="318" y="491">ENGLAND</tspan>
  </text>

  <text class="serif-caps" font-size="7.5">
    <tspan x="84" y="504">HANDCRAFTED</tspan>
    <tspan x="80" y="515">PREMIUM LIQUOR</tspan>
  </text>
  <text class="serif-caps" font-size="6.5" text-anchor="middle">
    <tspan x="208" y="498">APPROVED BY:</tspan>
    <tspan x="208" y="507">W. TRASKE</tspan>
  </text>
  <rect class="pattern-area" x="184" y="510" width="60" height="14" fill-opacity="0.6" role="img" aria-label="Handwritten signature of W. Traske"/>

  <!-- base band -->
  <line class="rule" x1="30" y1="528" x2="390" y2="528" stroke-width="1"/>
  <rect class="pattern-area" x="30" y="531" width="360" height="10" role="img" aria-label="Striped decorative border"/>
  <line class="rule" x1="30" y1="544" x2="390" y2="544" stroke-width="1"/>
</svg>
</body>
</html>
```